WP website design (Durham)

We need a wordpress design that will incorporate a professional color scheme with company logo in a clean layout. The design needs to consider that this will be developed on a responsive theme. Colors are undetermined - subdued or subtle, perhaps earth tones colors will likely work well. Logo color can be changed from black to any other to suit.

Client wants a unique look for their site - mentions liking http://www.rtvole.com/ and http://www.brunsikeauction.com/. Possible but not necessary to have large slideshow element.

Industry/Entity Type

It Company

Font styles to use
Serif
Sans Serif

Colors

Designer to choose colors to be used in the design.

Requirements
Must have
• Navigation: 1)Home 2) Auctions 3) For Sale 4) Buyers & Sellers 5) Brokerage 6) About Us 7) Contact Us

Site will have slideshow, please use high-end stock real estate image initially. Header will have logo. Social icons (Facebook, Twitter, Youtube) and tagline "THE REAL ESTATE AUCTION AUTHORITY SINCE 1977" will be used.

Widgets Include: Email signup form, Featured Auctions, News & Events Blog, Featured Video widget.

Footer will have contact info (below), site navigation, smaller company logo, testimonial widget, affiliation logos (attached).
Nice to have
• Site will have drop-down menus - please indicate the styling, for instance the dropdown menus 1) Referrals 2) Properties For Sale under the 'Brokerage' link

```html
<!DOCTYPE html>
<html lang="en">
<head>
<meta charset="utf-8">
<title>R. Whitcombe &amp; Associates – Real Estate Auctions</title>
<link rel="stylesheet" href="https://fonts.googleapis.com/css2?family=Arvo:wght@400;700&family=Montserrat:wght@400;500;600&family=Noto+Serif:ital@1&display=swap">
<style>
:root{
  --orange:#c0702c;
  --dark:#262626;
  --nav:#2b2b2b;
  --navy:#2e354b;
  --navy-deep:#262c3e;
  --grey:#e4e4e4;
  --mid:#6e6e6e;
  --text:#3a3a3a;
  --white:#ffffff;
  --footer:#3a3a3a;
}
*{box-sizing:border-box;margin:0;padding:0}
html,body{width:1020px;height:1200px;overflow:hidden;background:var(--white)}
body{position:relative;font-family:"Montserrat",sans-serif;color:var(--text)}
.abs{position:absolute}

/* header */
.brand{left:108px;top:20px;font-family:"Montserrat",sans-serif;font-size:26px;font-weight:400;color:#1d1d1d;letter-spacing:-0.5px}
.brand-sub{left:132px;top:53px;font-size:5px;letter-spacing:4px;color:#444}
.call{left:670px;top:28px;display:flex;align-items:center;gap:10px}
.call-text{font-size:13px;color:#333;line-height:19px}
.call-text b{font-size:14px;font-weight:500;display:block}
.social{left:845px;top:42px;display:flex;gap:6px}
.social span{width:18px;height:18px;background:#111;border-radius:3px}

/* nav */
.nav{left:0;top:87px;width:1020px;height:33px;background:var(--nav);display:flex;justify-content:center;gap:25px;align-items:center}
.nav a{color:var(--white);text-decoration:none;font-size:13px;font-weight:500}
.nav a.active{color:var(--orange)}
.dropdown{left:560px;top:128px;width:96px;padding:6px 6px 4px;background:#e8e8e8;border-radius:2px;z-index:5}
.dropdown::before{content:"";position:absolute;left:20px;top:-6px;border:6px solid transparent;border-top:0;border-bottom-color:#e8e8e8}
.dropdown span{display:block;font-size:6px;color:#fff;background:var(--dark);padding:3px 5px;margin-bottom:3px;border-radius:2px}
.dropdown span.on{background:var(--orange)}

/* hero */
.band{left:0;top:120px;width:1020px;height:262px;background:var(--navy)}
.frame{left:107px;top:129px;width:806px;height:286px;background:#d0d0d0;border-radius:4px;box-shadow:0 14px 18px -12px rgba(0,0,0,.35)}
.photo{left:118px;top:141px;width:784px;height:263px;background:linear-gradient(180deg,#8fb3d9 0%,#b9cbdb 38%,#8b8478 62%,#5d5a4e 82%,#3d5a2f 100%)}
.caption{left:135px;top:239px;width:275px;height:155px;background:rgba(40,40,40,.82);color:var(--white);padding:10px 20px}
.caption h1{font-family:"Arvo",serif;font-weight:700;font-size:14px;line-height:19px;text-align:center;letter-spacing:.3px}
.caption p{font-size:8.5px;line-height:14px;margin-top:12px}
.email{margin-top:8px;width:230px;height:24px;background:#d8d8d8;border:0;font-style:italic;font-size:10px;color:#555;padding:5px 11px}
.signup{display:inline-block;margin-top:8px;background:var(--orange);color:#fff;font-size:10px;padding:4px 10px;border-radius:2px}
.dots{left:474px;top:383px;display:flex;gap:5px}
.dots span{width:14px;height:14px;border-radius:50%;background:#8a8a8a}
.dots span.on{background:#111}

/* featured auctions */
.auctions{left:106px;top:462px;width:806px;height:260px;background:var(--dark);border-radius:5px 5px 0 0}
.auctions h2{position:absolute;top:18px;width:100%;text-align:center;font-family:"Arvo",serif;font-size:15px;color:#fff}
.lot{width:140px;text-align:center;color:#fff}
.thumb{width:115px;height:88px;margin:0 auto;border:4px solid #fff}
.lot h3{font-size:12px;font-weight:500;margin-top:8px}
.small-btns{margin-top:6px;display:flex;justify-content:center;gap:5px}
.small-btns span{font-size:6px;background:#5f5f5f;padding:4px 5px;border-radius:2px}
.bid{display:inline-block;margin-top:9px;background:var(--orange);font-size:7.5px;padding:4px 12px;border-radius:2px}
.arrow{width:38px;height:38px;border-radius:50%;background:#7a5532}

/* widgets */
.widgets{left:106px;top:722px;width:806px;height:304px;background:var(--grey)}
.card{top:762px;width:249px;height:218px;background:#fff;border:1px solid #d4d4d4;border-radius:4px;box-shadow:0 10px 10px -8px rgba(0,0,0,.3)}
.card h2{font-family:"Arvo",serif;font-weight:700;font-size:17px;text-align:center;margin-top:12px;color:#333}
.news{display:flex;gap:6px;padding:0 10px}
.date{width:31px;flex:none;text-align:center;font-size:11px}
.date .m{background:var(--orange);color:#222;padding:3px 0}
.date .d{background:var(--navy);color:#fff;padding:1px 0}
.news p{font-size:9px;line-height:15px;color:#444}
.news a{color:var(--orange);text-decoration:none}
.rule{height:1px;background:#ccc;margin:12px 10px}
.video{left:17px;top:61px;width:207px;height:122px;border:3px solid var(--orange);background:linear-gradient(180deg,#334466 0%,#8f7d6a 55%,#4a5f35 100%)}
.quote{font-family:"Noto Serif",serif;font-style:italic;font-size:10px;line-height:14px;color:#555}
.author{font-size:11px;color:#333;text-align:right}
.author b{font-weight:500;color:#2a4d7a}

/* footer */
.footer{left:0;top:1026px;width:1020px;height:133px;background:var(--footer);color:#fff}
.foot-logo{left:110px;top:37px;width:163px;height:47px;background:#fff;color:#1d1d1d;font-size:18px;display:flex;align-items:center;justify-content:center}
.contact{left:301px;top:28px;font-size:11px;line-height:20px}
.contact h3{font-size:15px;font-weight:500;margin-bottom:4px}
.contact div{display:flex;align-items:center;gap:7px}
.badges{left:664px;top:50px;display:flex;gap:10px;align-items:center}
.badges span{background:#e9e9e9;border-radius:3px}
.bottom{left:0;top:1159px;width:1020px;height:41px;background:var(--navy-deep);color:#fff;font-size:9.5px;font-weight:500}
.bottom nav{position:absolute;left:107px;top:15px;display:flex;gap:8px}
.bottom p{position:absolute;right:106px;top:15px}
</style>
</head>
<body>

<header>
  <div class="abs brand">R.WHITCOMBE</div>
  <div class="abs brand-sub">&amp; ASSOCIATES, INC.</div>
  <div class="abs call">
    <svg width="38" height="38" viewBox="0 0 38 38"><circle cx="19" cy="19" r="17" fill="none" stroke="#111" stroke-width="2.5"/><path d="M12 11c2-2 4 0 5 2s0 3-1 4c1 2 3 4 5 5 1-1 2-2 4-1s4 3 2 5c-2 2-5 2-9-1s-7-7-7-10c0-2 0-3 1-4z" fill="#111"/></svg>
    <div class="call-text">Call Now Today<b>(012) 555-0147</b></div>
  </div>
  <div class="abs social" aria-label="Social links"><span></span><span></span><span></span></div>
</header>

<nav class="abs nav">
  <a href="#">Home</a><a href="#">Auctions</a><a href="#">For Sale</a><a href="#">Buyer and Sellers</a><a href="#" class="active">Brokerage</a><a href="#">About Us</a><a href="#">Contact Us</a>
</nav>
<div class="abs dropdown"><span class="on">Lorem Ipsum Text</span><span>Lorem Ipsum Text</span><span>Lorem Ipsum Text</span></div>

<section>
  <div class="abs band"></div>
  <div class="abs frame"></div>
  <div class="abs photo" role="img" aria-label="Modern stone and glass luxury house with gardens"></div>
  <div class="abs caption">
    <h1>THE REAL ESTATE AUCTION AUTHORITY SINCE 1977</h1>
    <p>Lorem ipsum is a dummy text only. Dolor sit amet, consectetur adipiscing elit.</p>
    <input class="email" value="Enter Email Address" aria-label="Email">
    <br><span class="signup">Sign Up Now</span>
  </div>
  <div class="abs dots"><span></span><span class="on"></span><span></span><span></span></div>
</section>

<section class="abs auctions">
  <h2>FEATURED AUCTIONS</h2>
  <svg class="abs" style="left:26px;top:91px" width="38" height="38"><circle cx="19" cy="19" r="19" fill="#7a5532"/><path d="M23 10l-9 9 9 9" fill="none" stroke="#222" stroke-width="4"/></svg>
  <svg class="abs" style="left:742px;top:91px" width="38" height="38"><circle cx="19" cy="19" r="19" fill="#7a5532"/><path d="M15 10l9 9-9 9" fill="none" stroke="#222" stroke-width="4"/></svg>
  <div class="abs lot" style="left:111px;top:64px"><div class="thumb" role="img" aria-label="Grey suburban house with garage" style="background:linear-gradient(#9ab8d6,#6f7478 60%,#4f6a3c)"></div><h3>Pellentesque acsan</h3><div class="small-btns"><span>View Details</span><span>View Gallery</span></div><span class="bid">Click to bid online</span></div>
  <div class="abs lot" style="left:259px;top:64px"><div class="thumb" role="img" aria-label="White colonial house with porch" style="background:linear-gradient(#6fa3d8,#d8cfc2 55%,#5b7d3c)"></div><h3>Pellentesque acsan</h3><div class="small-btns"><span>View Details</span><span>View Gallery</span></div><span class="bid">Click to bid online</span></div>
  <div class="abs lot" style="left:407px;top:64px"><div class="thumb" role="img" aria-label="Yellow house with porch and garden" style="background:linear-gradient(#c6b78e,#d3b874 55%,#5c7b3a)"></div><h3>Pellentesque acsan</h3><div class="small-btns"><span>View Details</span><span>View Gallery</span></div><span class="bid">Click to bid online</span></div>
  <div class="abs lot" style="left:555px;top:64px"><div class="thumb" role="img" aria-label="Brick family home with two garages" style="background:linear-gradient(#a8c2db,#a08a72 55%,#526f36)"></div><h3>Pellentesque acsan</h3><div class="small-btns"><span>View Details</span><span>View Gallery</span></div><span class="bid">Click to bid online</span></div>
</section>

<div class="abs widgets"></div>

<article class="abs card" style="left:117px">
  <h2>Latest News &amp; Events</h2>
  <div class="news" style="margin-top:26px"><div class="date"><div class="m">Sep</div><div class="d">26</div></div><p>Lorem ipsum is a dummy text only. Dolor sit amet, consectetur adipiscing elit. Nullam felis mauris....<a href="#">[Read more]</a></p></div>
  <div class="rule"></div>
  <div class="news"><div class="date"><div class="m">Sep</div><div class="d">26</div></div><p>Lorem ipsum is a dummy text only. Dolor sit amet, consectetur adipiscing elit. Nullam felis mauris....<a href="#">[Read more]</a></p></div>
</article>

<article class="abs card" style="left:385px">
  <h2>Featured Video</h2>
  <div class="abs video" role="img" aria-label="Video still of a two-storey house">
    <svg class="abs" style="left:72px;top:22px" width="58" height="58"><circle cx="29" cy="29" r="26" fill="none" stroke="#fff" stroke-width="3"/><path d="M23 17l17 12-17 12z" fill="#fff"/></svg>
    <div class="abs" style="left:0;bottom:0;width:100%;height:12px;background:rgba(0,0,0,.6)"><div style="margin:5px 0 0 28px;width:60px;height:2px;background:#d33"></div></div>
  </div>
</article>

<article class="abs card" style="left:652px">
  <h2>Testimonials</h2>
  <svg class="abs" style="left:184px;top:57px" width="30" height="12"><rect width="11" height="11" fill="var(--orange)"/><path d="M7 3l-3 2.5 3 2.5" fill="none" stroke="#222"/><rect x="16" width="11" height="11" fill="var(--orange)"/><path d="M20 3l3 2.5-3 2.5" fill="none" stroke="#222"/></svg>
  <div class="abs" style="left:20px;top:72px;font-family:Arvo,serif;font-size:30px;color:var(--orange)">“</div>
  <p class="abs quote" style="left:50px;top:83px;width:175px">Lorem ipsum is a dummy text only. Dolor sit amet, consectetur adipiscing elit. Nullam felis mauris, eleifend ac rhoncus non, lobortis at diam.</p>
  <p class="abs author" style="left:50px;top:152px;width:175px"><b>John Doe</b>, New York</p>
</article>

<footer class="abs footer">
  <div class="abs foot-logo">R.WHITCOMBE</div>
  <div class="abs contact">
    <h3>R. Whitcombe &amp; Associates, Inc.</h3>
    <div>1245 Lorem Road, Dummy State 2465</div>
    <div><svg width="15" height="10"><rect x=".5" y=".5" width="14" height="9" fill="none" stroke="#fff"/><path d="M1 1l6.5 5 6.5-5" fill="none" stroke="#fff"/></svg>Email: rwhitcombe@info.com</div>
    <div><svg width="15" height="15"><circle cx="7.5" cy="7.5" r="6.5" fill="none" stroke="#fff"/><path d="M5 4c1-1 2 0 2 1l-1 1c0 1 1 2 2 2l1-1c1 0 2 1 1 2-1 1-3 1-5-1S4 5 5 4z" fill="#fff"/></svg>Phone: (631) 555-0182</div>
  </div>
  <div class="abs badges" aria-label="Affiliations">
    <span style="width:30px;height:34px"></span><span style="width:40px;height:30px"></span><span style="width:30px;height:34px"></span><span style="width:64px;height:26px"></span><span style="width:38px;height:30px"></span>
  </div>
</footer>

<div class="abs bottom">
  <nav><span>Home</span><span>Auctions</span><span>For Sale</span><span>Buyer and Sellers</span><span>Brokerage</span><span>About Us</span><span>Contact Us</span></nav>
  <p>Copyright©R.Whitcombe 2014. All Rights Reserved</p>
</div>

</body>
</html>
```